Cobalt Harbor Short Movie Poster

We need a poster designed for a short movie called 'Cobalt Harbor'. We will be using this on all social platforms & our promo material physically.
Have a look at www.cobaltharbormovie.com and check out both the 'Teaser' and 'The Script' pages to read the scripts so you get a feel for it and what it's about.

Target Market(s)

30-40 year old people who loved old mid to late 90's techno/trance (cobalt harbor, drizzle, ferrox Q, 482, wait for me by the tin lantern)

Industry/Entity Type

Entertainment

Colors

Designer to choose colors to be used in the design.

Requirements
Must have
• Main character, dancing, some resemblance to music and outer space.
Nice to have
• An element of humour.

```html
<!DOCTYPE html>
<html lang="en">
<head>
<meta charset="utf-8">
<title>Cobalt Harbor – Short Movie Poster</title>
<link rel="stylesheet" href="https://fonts.googleapis.com/css2?family=Orbitron:wght@800;900&family=Exo+2:wght@400&display=swap">
<style>
  :root {
    --page-bg: #ffffff;
    --space-deep: #0a0514;
    --space-violet: #2a1160;
    --nebula-pink: #e0207e;
    --nebula-blue: #3b2bd0;
    --moon-light: #fbe3ee;
    --moon-pink: #eb8fb6;
    --title-copper: #e39682;
    --title-glow: #ff2a3a;
    --streak-cyan: #29c3ff;
    --credit-white: #ffffff;
    --planet-red: #8a3452;
    --planet-blue: #5a5aa0;
    --small-moon: #bfe4ff;
  }
  html, body {
    margin: 0;
    width: 1200px;
    height: 1200px;
    overflow: hidden;
    background: var(--page-bg);
  }
  .poster {
    position: absolute;
    left: 187px;
    top: 30px;
    width: 826px;
    height: 1140px;
    box-shadow: 0 10px 40px rgba(0,0,0,0.45);
    overflow: hidden;
  }
  .poster svg { display: block; }
  .title-text {
    font-family: "Orbitron", sans-serif;
    font-weight: 900;
    fill: var(--title-copper);
    letter-spacing: 2px;
  }
  .credit-text {
    font-family: "Exo 2", sans-serif;
    font-size: 24px;
    fill: var(--credit-white);
  }
</style>
</head>
<body>
<div class="poster">
  <svg width="826" height="1140" viewBox="0 0 826 1140" xmlns="http://www.w3.org/2000/svg">
    <defs>
      <linearGradient id="spaceBase" x1="0" y1="0" x2="0" y2="1">
        <stop offset="0" stop-color="var(--space-violet)"/>
        <stop offset="0.5" stop-color="#1a0a2e"/>
        <stop offset="1" stop-color="var(--space-deep)"/>
      </linearGradient>
      <radialGradient id="nebulaGlow" cx="0.5" cy="0.45" r="0.55">
        <stop offset="0" stop-color="var(--nebula-pink)" stop-opacity="0.9"/>
        <stop offset="0.45" stop-color="#8a1a9a" stop-opacity="0.55"/>
        <stop offset="1" stop-color="var(--nebula-blue)" stop-opacity="0"/>
      </radialGradient>
      <radialGradient id="moonFill" cx="0.5" cy="0.5" r="0.5">
        <stop offset="0" stop-color="#ffffff"/>
        <stop offset="0.6" stop-color="var(--moon-light)"/>
        <stop offset="1" stop-color="var(--moon-pink)"/>
      </radialGradient>
      <radialGradient id="planetRed" cx="0.55" cy="0.35" r="0.7">
        <stop offset="0" stop-color="#a7506c"/>
        <stop offset="1" stop-color="#3a1230"/>
      </radialGradient>
      <radialGradient id="planetBlue" cx="0.4" cy="0.35" r="0.7">
        <stop offset="0" stop-color="#8a7fb8"/>
        <stop offset="1" stop-color="#2c2456"/>
      </radialGradient>
      <radialGradient id="smallMoon" cx="0.5" cy="0.5" r="0.5">
        <stop offset="0" stop-color="#e8f6ff"/>
        <stop offset="1" stop-color="var(--small-moon)"/>
      </radialGradient>
      <linearGradient id="streakCyan" x1="0" y1="0" x2="1" y2="0">
        <stop offset="0" stop-color="#ffffff" stop-opacity="0.9"/>
        <stop offset="0.4" stop-color="var(--streak-cyan)"/>
        <stop offset="1" stop-color="var(--streak-cyan)" stop-opacity="0.2"/>
      </linearGradient>
      <linearGradient id="streakViolet" x1="0" y1="0" x2="1" y2="0">
        <stop offset="0" stop-color="#6a4cff" stop-opacity="0.2"/>
        <stop offset="1" stop-color="#8a6cff"/>
      </linearGradient>
      <filter id="titleGlow" x="-20%" y="-50%" width="140%" height="200%">
        <feGaussianBlur in="SourceAlpha" stdDeviation="7"/>
        <feFlood flood-color="#ff2a3a" flood-opacity="0.8"/>
        <feComposite operator="in" in2="SourceAlpha"/>
        <feMerge><feMergeNode/><feMergeNode in="SourceGraphic"/></feMerge>
      </filter>
      <filter id="soft"><feGaussianBlur stdDeviation="6"/></filter>
    </defs>

    <rect class="space-backdrop" width="826" height="1140" fill="url(#spaceBase)" role="img" aria-label="Starfield of deep violet outer space"/>
    <ellipse class="nebula" cx="420" cy="460" rx="420" ry="420" fill="url(#nebulaGlow)" role="img" aria-label="Pink and violet nebula glow"/>

    <!-- horizon light streaks -->
    <line class="streak" x1="0" y1="182" x2="670" y2="182" stroke="#6f5cff" stroke-width="2" opacity="0.8"/>
    <ellipse class="flare" cx="420" cy="182" rx="55" ry="12" fill="#ffd0ee" filter="url(#soft)"/>
    <circle class="flare-core" cx="420" cy="182" r="9" fill="#ffffff"/>

    <circle class="moon" cx="401" cy="477" r="219" fill="url(#moonFill)" role="img" aria-label="Large glowing pink moon"/>

    <rect class="streak-band" x="0" y="593" width="300" height="18" fill="url(#streakViolet)" transform="scale(-1,1) translate(-300,0)"/>
    <rect class="streak-band" x="520" y="593" width="306" height="16" fill="url(#streakCyan)"/>
    <line class="streak" x1="0" y1="516" x2="826" y2="516" stroke="#8a6cff" stroke-width="2" opacity="0.7"/>

    <g class="title" transform="rotate(-15 405 480)" filter="url(#titleGlow)">
      <line x1="110" y1="395" x2="720" y2="395" stroke="#ffffff" stroke-width="1.5" opacity="0.8"/>
      <text class="title-text" x="425" y="463" font-size="78" text-anchor="middle">COBALT</text>
      <text class="title-text" x="400" y="548" font-size="78" text-anchor="middle">HARBOR</text>
      <line x1="110" y1="580" x2="720" y2="580" stroke="#ffffff" stroke-width="1.5" opacity="0.8"/>
    </g>

    <circle class="planet planet-right" cx="770" cy="865" r="76" fill="url(#planetBlue)" role="img" aria-label="Blue cloudy planet"/>
    <circle class="planet planet-left" cx="119" cy="1025" r="126" fill="url(#planetRed)" role="img" aria-label="Crimson cloudy planet"/>
    <circle class="small-moon" cx="412" cy="975" r="30" fill="url(#smallMoon)" role="img" aria-label="Small pale blue moon"/>

    <text class="credit-text" x="751" y="1086" text-anchor="end">Written by Milo Hartcastle &amp; Jonah Pereira</text>
  </svg>
</div>
</body>
</html>
```